Personal Training Studio Checkin App (or URL based)

I would like a simple web based app built for our  business. We have a training studio with a simple business model. All our clients buy sessions in packages either 4, 8, or 12 at a time. We want something that a trainer can pull up and Check in a client. This will record the date and time the client was checked in, by what trainer, and what type of session. This system will keep track of the following:
Whenever a Client Checks in so it will ‘tick off’ a session on their package (ie- they have gone from 11 sessions left to 10 sessions left)
Track what sessions a particular trainer does so we can pay them at the end of the week and look at who they trained, what type of session and how many
Look at client activity: Every time they check in, Recharge their package, any activity related to the client, even if it was admin – like deleting a session that was mistakenly recorded.
This will keep a database of clients added and all their activity
The pdf I have included lays out how I think it would work and the features I want
I would like this to run off an tablora that we have at our front check in counter. It can be an app or a URL that use.
***THIS PROJECT IS NOT SO MUCH ABOUT DESIGN BUT ABOUT FUNCTIONALITY OF THE APPLICATION. IT MUST HAVE THE FEATURES I HAVE ASKED FOR THAT WORK TOGETHER. I AM WILLING TO PAY A LITTLE MORE AS A BONUS IF YOU CAN ACCOMPLISH THIS. ALSO IF I FIN THE RIGHT PERSON THAT CAN DO THIS I WILL MAKE IT A GUARNTEED PROJECT.

- Functionality and Track and record all the info we need

```html
<!DOCTYPE html>
<html lang="en">
<head>
<meta charset="utf-8">
<title>Corelane Personal Training Studio – Add New Client Page</title>
<link href="https://fonts.googleapis.com/css2?family=DM+Sans:wght@400;500;700&family=Inter:wght@400;500;600&display=swap" rel="stylesheet">
<style>
  :root {
    --stage: #4a4a4a;
    --stage-text: #ffffff;
    --card: #f8f8f8;
    --white: #ffffff;
    --line: #e3e3e3;
    --field-line: #d9d9d9;
    --ink: #1d1d1d;
    --muted: #6b6b6b;
    --placeholder: #8a8a8a;
    --accent: #e36f0b;
    --accent-soft: #f0f0f0;
    --required: #e0302b;
  }
  * { box-sizing: border-box; margin: 0; padding: 0; }
  html, body { width: 1200px; height: 1200px; overflow: hidden; }
  body { background: var(--stage); font-family: "Inter", sans-serif; color: var(--ink); position: relative; }

  .deck-title { position: absolute; left: 55px; top: 50px; font-family: "DM Sans", sans-serif; color: var(--stage-text); font-size: 27px; line-height: 32px; }
  .deck-title strong { font-weight: 700; display: block; }
  .deck-title span { font-weight: 400; display: block; }
  .page-name { position: absolute; right: 55px; top: 50px; text-align: right; font-family: "DM Sans", sans-serif; font-weight: 700; color: var(--stage-text); font-size: 27px; line-height: 32px; }

  .app-card { position: absolute; left: 28px; top: 147px; width: 1144px; height: 802px; background: var(--card); border-radius: 25px; overflow: hidden; }
  .topbar { position: absolute; left: 0; top: 0; width: 100%; height: 60px; background: var(--white); border-bottom: 1px solid var(--line); }
  .brand { position: absolute; left: 24px; top: 17px; display: flex; align-items: center; gap: 8px; font-weight: 600; font-size: 22px; letter-spacing: 1px; color: #555; }
  .brand-mark { width: 18px; height: 18px; background: var(--accent); }
  .avatar { position: absolute; right: 16px; top: 12px; width: 32px; height: 32px; border-radius: 50%; background: #111; color: #fff; font-size: 13px; display: flex; align-items: center; justify-content: center; }

  .nav { position: absolute; left: 15px; top: 88px; width: 270px; }
  .nav-item { height: 39px; margin-bottom: 4px; display: flex; align-items: center; gap: 13px; padding-left: 10px; font-size: 14px; color: #333; border-radius: 6px; }
  .nav-item svg { width: 20px; height: 20px; stroke: #888; fill: none; stroke-width: 1.4; }
  .nav-item.is-active { background: var(--accent-soft); color: var(--accent); }
  .nav-item.is-active svg { stroke: var(--accent); }

  .form-panel { position: absolute; left: 345px; top: 60px; width: 782px; height: 653px; background: var(--white); border: 1px solid var(--line); border-top: none; border-radius: 0 0 12px 12px; }
  .steps { position: absolute; left: 0; top: 0; width: 100%; height: 61px; border-bottom: 1px solid var(--line); }
  .step { position: absolute; top: 0; height: 60px; display: flex; align-items: center; gap: 16px; font-size: 14px; }
  .step-dot { width: 40px; height: 40px; border-radius: 50%; display: flex; align-items: center; justify-content: center; font-size: 14px; }
  .step-done .step-dot { background: var(--accent); }
  .step-current { color: var(--accent); }
  .step-current .step-dot { border: 1.5px solid var(--accent); }
  .step-divider { position: absolute; left: 370px; top: 0; }

  .toggle-row { position: absolute; left: 24px; top: 85px; display: flex; align-items: center; gap: 12px; font-size: 14px; }
  .toggle { width: 43px; height: 25px; border-radius: 13px; background: var(--accent); position: relative; }
  .toggle::after { content: ""; position: absolute; right: 3px; top: 3px; width: 19px; height: 19px; border-radius: 50%; background: #fff; }

  .label { position: absolute; font-size: 14px; font-weight: 500; }
  .req { color: var(--required); font-size: 10px; vertical-align: top; }
  .field { position: absolute; height: 37px; border: 1px solid var(--field-line); border-radius: 7px; background: #fff; font-size: 14px; display: flex; align-items: center; padding-left: 12px; box-shadow: 0 1px 1px rgba(0,0,0,.03); }
  .field.select svg { position: absolute; right: 12px; top: 13px; }
  .field .placeholder { color: var(--placeholder); }

  .partner-box { position: absolute; left: 24px; top: 325px; width: 734px; height: 244px; border: 1px solid var(--line); border-radius: 10px; }
  .partner-legend { position: absolute; left: 16px; top: -9px; background: #fff; padding: 0 8px; font-size: 14px; font-weight: 500; }
  .hint { position: absolute; left: 24px; top: 112px; font-size: 13px; color: var(--muted); }

  .btn { position: absolute; height: 36px; border: 1px solid var(--field-line); border-radius: 7px; background: #fff; font-size: 14px; font-weight: 600; display: flex; align-items: center; justify-content: center; }
  .btn-primary { background: var(--accent); border-color: var(--accent); color: #fff; }

  .caption { position: absolute; left: 0; top: 1028px; width: 1200px; text-align: center; font-family: "DM Sans", sans-serif; font-size: 23px; line-height: 28px; color: var(--stage-text); }
</style>
</head>
<body>
  <header class="deck-title"><strong>Corelane Personal Training Studio</strong><span>Frontdesk Web App</span></header>
  <div class="page-name">Add New Client<br>Page</div>

  <main class="app-card">
    <div class="topbar">
      <div class="brand"><span class="brand-mark"></span>CORELANE</div>
      <div class="avatar">A</div>
    </div>

    <nav class="nav">
      <div class="nav-item"><svg viewBox="0 0 20 20"><path d="M3 9 10 3l7 6v8H3z"/><path d="M8 17v-5h4v5"/></svg>Dashboard</div>
      <div class="nav-item is-active"><svg viewBox="0 0 20 20"><circle cx="10" cy="6" r="2.5"/><circle cx="4.5" cy="8" r="2"/><circle cx="15.5" cy="8" r="2"/><path d="M5.5 16c0-3 2-5 4.5-5s4.5 2 4.5 5zM1.5 15c0-2 1.3-3.5 3-3.5M18.5 15c0-2-1.3-3.5-3-3.5"/></svg>Clients</div>
      <div class="nav-item"><svg viewBox="0 0 20 20"><rect x="4" y="4" width="12" height="14" rx="1.5"/><rect x="7.5" y="2.5" width="5" height="3" rx=".8"/><path d="M7 9h6M7 12h6M7 15h4"/></svg>Session Logs</div>
      <div class="nav-item"><svg viewBox="0 0 20 20"><rect x="2.5" y="2.5" width="6" height="6" rx="2"/><rect x="11.5" y="2.5" width="6" height="6" rx="2"/><rect x="2.5" y="11.5" width="6" height="6" rx="2"/><rect x="11.5" y="11.5" width="6" height="6" rx="2"/></svg>Session Types</div>
      <div class="nav-item"><svg viewBox="0 0 20 20"><circle cx="10" cy="10" r="8"/><circle cx="10" cy="8" r="3"/><path d="M4.8 15.8c1.2-2 3-3 5.2-3s4 1 5.2 3"/></svg>Trainers</div>
    </nav>

    <section class="form-panel">
      <div class="steps">
        <div class="step step-done" style="left:24px"><span class="step-dot"><svg width="18" height="14" viewBox="0 0 18 14"><path d="M1 7l5 5L17 1" stroke="#fff" stroke-width="1.6" fill="none"/></svg></span>Client Details</div>
        <svg class="step-divider" width="16" height="61" viewBox="0 0 16 61"><path d="M1 0l13 30L1 61" stroke="#ddd" fill="none"/></svg>
        <div class="step step-current" style="left:412px"><span class="step-dot">02</span>Initial Package</div>
      </div>

      <div class="toggle-row"><span class="toggle"></span>Purchase Initial Package?</div>

      <div class="label" style="left:24px;top:141px">Session Type</div>
      <div class="field select" style="left:24px;top:163px;width:736px">Partner Session<svg width="12" height="8" viewBox="0 0 12 8"><path d="M1 1l5 5 5-5" stroke="#444" stroke-width="1.5" fill="none"/></svg></div>

      <div class="label" style="left:24px;top:232px">Starting Package Session Amount</div>
      <div class="field" style="left:24px;top:253px;width:736px"></div>

      <fieldset class="partner-box">
        <div class="partner-legend">Partner Details</div>
        <div class="label" style="left:24px;top:38px">Existing Partner</div>
        <div class="field select" style="left:23px;top:66px;width:333px"><span class="placeholder">Select an option</span><svg width="12" height="8" viewBox="0 0 12 8"><path d="M1 1l5 5 5-5" stroke="#444" stroke-width="1.5" fill="none"/></svg></div>
        <div class="hint">If partner is not in the list, fill their details next.</div>
        <div class="label" style="left:379px;top:38px">Partner's Full Name<span class="req">*</span></div>
        <div class="field" style="left:378px;top:66px;width:332px"></div>
        <div class="label" style="left:24px;top:156px">Partner's Email<span class="req">*</span></div>
        <div class="field" style="left:23px;top:184px;width:333px"></div>
        <div class="label" style="left:379px;top:156px">Partner's Phone<span class="req">*</span></div>
        <div class="field" style="left:378px;top:184px;width:332px"></div>
      </fieldset>

      <div class="btn" style="left:24px;top:593px;width:57px">Back</div>
    </section>

    <div class="btn btn-primary" style="left:345px;top:735px;width:68px">Create</div>
    <div class="btn" style="left:425px;top:735px;width:183px">Create &amp; create another</div>
    <div class="btn" style="left:618px;top:735px;width:71px">Cancel</div>
  </main>

  <p class="caption">Direct package registration available for new clients.<br>"Partner Session" selection allows simultaneous partner registration<br>or linking to an existing client.</p>
</body>
</html>
```